Banner for homepage

It is a new banner for the homepage, temporary site address is 61.187.40.72 ( is the biggest banner only ) . Would be 5 variations for image content as below (in Portuguese ) :

Image 1:
Leitor de codigo de barras
Todos os tipos de leitores de código de barras para as mais diversas aplicações.
( example of product images in : http://www.quentorlabs.com/en-US/Pages/Category.aspx?category=barcode-scanners&cat=KLT)

Image 2:
Impressora de etiquetas
Identifique o que for nessário com o melhor custo/beneficio e flexibilidade de materiais de impressão.
( example of product images in : vintor.com in label printers desktop and industrial)

Image 3:
Impressora de cupom
Imprima recibos e cupons fiscais com agilidade e qualidade, temos a impressora certa para o seu PDV.
( example of product images in : http://www.palutrek.com.br/equipamento-categoria-impressoras+fiscais.html)

Image 4:
Coletor de dados
Computadores móveis com leitor de código de barras, que levam a automação para frente de trabalho.
( example of product images in : http://www.quentorlabs.com/en-US/Pages/Category.aspx?cat=KLT&category=hand-held-mobile-computer)

Image 5:
Etiquetas e Ribbons:
Etiquetas adesivas e não adesivas em vários de tipos de materiais, papéis e plásticos. O ribbon certo para impressão perfeita em cada material.
( example of product images in : http://www.tagmirelo.com/cats/supplies/barcode-printer.htm?nav=hdr)

```html
<!DOCTYPE html>
<html lang="pt-BR">
<head>
<meta charset="utf-8">
<title>Leitor de código de barras</title>
<link rel="stylesheet" href="https://fonts.googleapis.com/css2?family=PT+Sans:wght@700&family=Arimo:wght@400;700&display=swap">
<style>
  :root {
    --bg-light: #e9eaeb;
    --bg-mid: #c9cbcd;
    --bg-dark: #a9acaf;
    --floor: #d6d7d8;
    --title-top: #ff8a3a;
    --title-bottom: #d61a0a;
    --text-dark: #111111;
    --button-top: #e23a30;
    --button-bottom: #8e0c08;
    --button-text: #ffffff;
    --product-dark: #3f4347;
    --product-mid: #6a6f74;
  }
  * { margin: 0; padding: 0; box-sizing: border-box; }
  html, body { width: 1200px; height: 549px; overflow: hidden; }
  .banner {
    position: relative;
    width: 1200px;
    height: 549px;
    overflow: hidden;
    background:
      radial-gradient(ellipse 300px 260px at 1000px 0px, rgba(255,255,255,0.95), rgba(255,255,255,0) 70%),
      radial-gradient(ellipse 700px 420px at 420px 250px, var(--bg-light), rgba(233,234,235,0) 75%),
      linear-gradient(90deg, var(--bg-mid) 0%, var(--bg-light) 45%, var(--bg-mid) 75%, var(--bg-dark) 100%);
  }
  .banner__floor {
    position: absolute;
    left: 0; right: 0; top: 420px; bottom: 0;
    background: linear-gradient(180deg, rgba(255,255,255,0.35) 0%, var(--floor) 40%, var(--bg-mid) 100%);
  }
  .banner__title {
    position: absolute;
    left: 38px;
    top: 92px;
    font-family: "PT Sans", "Trebuchet MS", sans-serif;
    font-weight: 700;
    font-size: 62px;
    line-height: 1;
    letter-spacing: 0.2px;
    background: linear-gradient(180deg, var(--title-top) 0%, #f2541c 50%, var(--title-bottom) 100%);
    -webkit-background-clip: text;
    background-clip: text;
    color: transparent;
    -webkit-text-stroke: 1px rgba(255,255,255,0.7);
    filter: drop-shadow(1px 2px 2px rgba(0,0,0,0.35));
  }
  .banner__lead {
    position: absolute;
    left: 38px;
    top: 184px;
    width: 720px;
    font-family: "Arimo", Arial, sans-serif;
    font-size: 28px;
    line-height: 35px;
    color: var(--text-dark);
  }
  .banner__cta {
    position: absolute;
    left: 66px;
    top: 441px;
    width: 225px;
    height: 64px;
    display: flex;
    align-items: center;
    gap: 16px;
    padding-left: 10px;
    border-radius: 32px;
    background: linear-gradient(180deg, var(--button-top) 0%, #c01a14 50%, var(--button-bottom) 100%);
    box-shadow: 0 3px 6px rgba(0,0,0,0.4), inset 0 1px 0 rgba(255,255,255,0.4);
    font-family: "Arimo", Arial, sans-serif;
    font-size: 27px;
    color: var(--button-text);
    text-decoration: none;
  }
  .banner__cta-icon { width: 44px; height: 44px; flex: none; }
  .banner__product {
    position: absolute;
    left: 840px;
    top: 146px;
    width: 292px;
    height: 362px;
    border-radius: 40px 40px 60px 60px;
    background: radial-gradient(ellipse at 45% 35%, var(--product-mid), var(--product-dark) 70%);
  }
</style>
</head>
<body>
  <section class="banner">
    <div class="banner__floor"></div>
    <h1 class="banner__title">Leitor de codigo de barras</h1>
    <p class="banner__lead">Todos os tipos de leitores de código de barras para as mais diversas aplicações.</p>
    <a class="banner__cta" href="#">
      <svg class="banner__cta-icon" viewBox="0 0 44 44" aria-hidden="true">
        <circle cx="22" cy="22" r="20" fill="#a31109" stroke="#ffffff" stroke-opacity="0.5" stroke-width="2"/>
        <path d="M17 13 L31 22 L17 31 Z" fill="#ffffff"/>
      </svg>
      Veja Mais
    </a>
    <div class="banner__product" role="img" aria-label="Leitor de código de barras sem fio de mão, cinza escuro, apoiado em sua base"></div>
  </section>
</body>
</html>
```